The Marble Lantern Company Ltd. Needs a Facebook Design. An Event & Wedding Company

We need a WOW Facebook design. Focusing on catching people's attention. We don't want it all wedding like Facebook because we do want to focus on events too.

We currently have an underconstruction website up. feel free to check it out.

Http://www.themarblelantern.com

An attachment of our logo is attached below

Be Creative!!

Target Market(s)

Companies & Couples who's getting married or engaged 

Industry/Entity Type

Wedding

Font styles to use
Serif
Sans Serif
Decorative
Script

Colors

Designer to choose colors to be used in the design.

Requirements
Must have
• VERY VERY CREATIVE! CATCHY!
Should not have
• nothing really boring. anything green!

```html
<!DOCTYPE html>
<html lang="en">
<head>
<meta charset="utf-8">
<title>The Marble Lantern — Events &amp; Wedding</title>
<link rel="stylesheet" href="https://fonts.googleapis.com/css2?family=Josefin+Sans:wght@300;400&display=swap">
<style>
  :root {
    --ink: #1e1e1e;
    --rule: #2a2a2a;
    --gold: #b98f3e;
    --photo-dark: #bdbdbd;
    --photo-mid: #dcdcdc;
    --photo-light: #f5f5f5;
  }
  html, body {
    margin: 0;
    padding: 0;
    overflow: hidden;
    background: #ffffff;
  }
  .cover {
    position: relative;
    width: 1200px;
    height: 444px;
    overflow: hidden;
    font-family: "Josefin Sans", sans-serif;
    color: var(--ink);
  }
  .cover__backdrop {
    position: absolute;
    inset: 0;
    background:
      radial-gradient(ellipse 420px 260px at 340px 160px, rgba(120,120,120,0.45), rgba(120,120,120,0) 70%),
      radial-gradient(ellipse 300px 200px at 180px 380px, rgba(160,160,160,0.35), rgba(160,160,160,0) 70%),
      linear-gradient(90deg, var(--photo-dark) 0%, var(--photo-mid) 35%, var(--photo-light) 70%, var(--photo-mid) 100%);
  }
  .cover__wash {
    position: absolute;
    inset: 0;
    background: rgba(255,255,255,0.35);
  }
  .brand-block {
    position: absolute;
    inset: 0;
  }
  .brand-block__rules {
    position: absolute;
    left: 0;
    top: 0;
  }
  .brand-block__name {
    position: absolute;
    left: 0;
    right: 0;
    top: 152px;
    margin: 0;
    text-align: center;
    font-weight: 300;
    font-size: 54px;
    letter-spacing: 0.12em;
    line-height: 1;
    text-transform: uppercase;
    color: var(--ink);
  }
  .brand-block__tagline {
    position: absolute;
    left: 0;
    right: 0;
    top: 268px;
    margin: 0;
    text-align: center;
    font-weight: 400;
    font-size: 21px;
    letter-spacing: 0.62em;
    padding-left: 0.62em;
    line-height: 1;
    text-transform: uppercase;
    color: var(--ink);
  }
</style>
</head>
<body>
  <main class="cover">
    <div class="cover__backdrop" role="img" aria-label="Soft, washed-out black and white photograph of an elegant banquet table with a floral centrepiece, glassware and white chiavari chairs"></div>
    <div class="cover__wash"></div>

    <section class="brand-block">
      <svg class="brand-block__rules" width="1200" height="444" viewBox="0 0 1200 444" aria-hidden="true">
        <line x1="204" y1="99" x2="1018" y2="99" stroke="var(--rule)" stroke-width="1.4"/>
        <line x1="204" y1="350" x2="586" y2="350" stroke="var(--rule)" stroke-width="1.4"/>
        <line x1="656" y1="350" x2="1018" y2="350" stroke="var(--rule)" stroke-width="1.4"/>
        <circle cx="621" cy="350" r="9" fill="var(--gold)"/>
      </svg>
      <h1 class="brand-block__name">The Marble Lantern</h1>
      <p class="brand-block__tagline">Events &amp; Wedding</p>
    </section>
  </main>
</body>
</html>
```